Business Card Design

Hello,
I try and keep my business card fresh and current. So about every year i get a new one. This year I'd like something with a white background and black lettering.
Before you start - I do not want my phone number or any other description on the card other than my url and my email.

I'd like a double sided business card with
TobFarnsby.com on one side

and

Tob@TobFarnsby.com on the other side of the card

Thinking very minimalistic and modern.
I don't have a particular font i mind or how to capitalize my name or website. This card will lead people to my new website that is being designed to showcase my photography and music.

* Initial thought was the front side of the card having a grid-like pattern built out of dashes or periods, with my website sitting within the pattern and on the back side my email on a stark white background. But that might look completely lame - haha.

I'm looking forward to seeing what you come up with.

thank you,
- tob farnsby

Reason: Want to spend some more time with the designs and add a little $. thanks for all the designs - tob

Wanted to add a little $ and spend some more time with the designs.

big thanks to all who have submitted work 

- tob

Industry/Entity Type

Business

Contact Information for Business Card

www.tobfarnsby.com
tob@tobfarnsby.com

Colors
000000
ffffff

Requirements
Must have
• tobfarnsby.com
tob@tobfarnsby.com
Should not have
• phone number
any description of what i do, photography or music

```html
<!DOCTYPE html>
<html lang="en">
<head>
<meta charset="utf-8">
<title>Tob Farnsby — Business Card</title>
<link rel="stylesheet" href="https://fonts.googleapis.com/css2?family=Courier+Prime&display=swap">
<style>
  :root {
    --ink: #000000;
    --paper: #ffffff;
    --backdrop: #2d2b2a;
    --dot-tone: #efefef;
  }
  * { margin: 0; padding: 0; box-sizing: border-box; }
  html, body {
    width: 1200px;
    height: 1200px;
    overflow: hidden;
    background: var(--backdrop);
  }
  .stage {
    width: 1200px;
    height: 1200px;
    display: flex;
    flex-direction: column;
    align-items: center;
    justify-content: center;
    gap: 60px;
  }
  .card {
    position: relative;
    width: 880px;
    height: 503px;
    background: var(--paper);
    overflow: hidden;
  }
  .card-text {
    position: absolute;
    font-family: "Courier Prime", "Courier New", monospace;
    font-size: 27px;
    letter-spacing: 0.5px;
    color: var(--ink);
  }
  .card--back .email {
    left: 88px;
    top: 104px;
  }
  .dot-grid {
    position: absolute;
    inset: 0;
    background: var(--dot-tone);
  }
  .card--front .website {
    right: 78px;
    bottom: 52px;
  }
</style>
</head>
<body>
  <main class="stage">
    <section class="card card--back">
      <p class="card-text email">Tob@TobFarnsby.com</p>
    </section>
    <section class="card card--front">
      <div class="dot-grid" role="img" aria-label="Fine black dot grid pattern covering the card"></div>
      <p class="card-text website">TobFarnsby.com</p>
    </section>
  </main>
</body>
</html>
```